Etiketten-Design für Kräuterbonbon-Metalldose
Marlene Vosk hat sehr viel Talent. Das Design ist absolut kreativ.
Zielgruppe
Unsere Firma VelbraCor verkauft verschiedene Sorten Kräuterbonbons.
Wir brauchen ein Etikett, dass auf eine Metall-Dose (Durchmesser 10 cam, Höhe ca. 3 cm) geklebt wird.
Zielgruppe: jung-alt
Aufgabenstellung
Der Name unserer Kräuterbonbons ist Pfeffling.
Wir möchten, dass unsere Kunden, wenn sie das Etikett sehen einen Bezug zur Schweiz herstellen können.
Wir verwenden für unsere Bonbons unterschiedliche Kräuter für verschiedene Anwendungen:
Konkret sind erstmal 4 Dosen geplant:
-Kräutermischung aus 16 Kräuter gegen Husten
-Salbei gegen Halsschmerzen
-Anis gegen Magenschmerzen
-Zitrone/Ingwer für die Nerven
Vorderseite: Produktbeschreibung
Rückseite: unsere Herstellerangaben
Größenangaben der Dose: Durchmesser 10 cm, Höhe ca. 3 cm
Im Anhang habe ich Ihnen noch weitere/ genauere Informationen zur Verfügung bereitgestellt!

```html
<!DOCTYPE html>
<html lang="de">
<head>
<meta charset="utf-8">
<title>Pfeffling – Dosenetiketten</title>
<link rel="stylesheet" href="https://fonts.googleapis.com/css2?family=Caveat+Brush&family=Montserrat:wght@500&display=swap">
<style>
  :root{
    --paper:#ffffff;
    --swiss-red:#e30613;
    --sage:#92926d;
    --anise:#2596a0;
    --ginger:#f8b552;
    --ink-light:#ffffff;
  }
  html,body{margin:0;padding:0;overflow:hidden;}
  body{width:1200px;height:2678px;background:var(--paper);position:relative;}
  .brand-mark,.label{position:absolute;display:block;}
  .brand-mark{left:420px;top:110px;width:320px;height:270px;}
  .label{left:277px;width:600px;height:600px;}
  .label--salbei{top:497px;}
  .label--anis{top:1197px;}
  .label--ingwer{top:1895px;}
  .brand-name{font-family:"Caveat Brush",cursive;fill:var(--swiss-red);font-size:44px;letter-spacing:4px;}
  .claim{font-family:"Montserrat",sans-serif;font-weight:500;fill:var(--swiss-red);font-size:19px;letter-spacing:.5px;}
  .flavour{font-family:"Caveat Brush",cursive;fill:var(--ink-light);font-size:130px;letter-spacing:6px;}
  .flavour--long{font-size:118px;letter-spacing:4px;}
  .use-case{font-family:"Caveat Brush",cursive;fill:var(--ink-light);font-size:46px;letter-spacing:5px;}
  .brand-dot{fill:var(--swiss-red);}
  .herb-area{fill:#ffffff;opacity:.22;}
</style>
</head>
<body>

<svg class="brand-mark" viewBox="-160 -155 320 270" aria-label="Pfeffling">
  <defs><path id="arc-top-name" d="M -128 10 A 130 130 0 0 1 70 -110"/></defs>
  <circle class="brand-dot" cx="0" cy="0" r="92"/>
  <text class="brand-name"><textPath href="#arc-top-name">PFEFFLING</textPath></text>
</svg>

<svg class="label label--salbei" viewBox="-300 -300 600 600">
  <defs>
    <path id="s-name" d="M -128 10 A 130 130 0 0 1 70 -110"/>
    <path id="s-claim" d="M -185 10 A 185 185 0 0 1 100 -158"/>
    <path id="s-flavour" d="M -250 50 A 255 255 0 0 0 245 70"/>
    <path id="s-use" d="M 225 150 A 270 270 0 0 0 10 -270"/>
  </defs>
  <circle cx="0" cy="0" r="297" fill="var(--sage)"/>
  <ellipse class="herb-area" cx="-175" cy="90" rx="85" ry="60" role="img" aria-label="Zeichnung eines Salbeizweigs"/>
  <text class="claim"><textPath href="#s-claim">TRADITIONAL SWISS FORMULA</textPath></text>
  <circle class="brand-dot" cx="3" cy="3" r="92"/>
  <text class="brand-name"><textPath href="#s-name">PFEFFLING</textPath></text>
  <text class="flavour" text-anchor="middle"><textPath href="#s-flavour" startOffset="50%">SALBEI</textPath></text>
  <text class="use-case"><textPath href="#s-use">BEI HALSSCHMERZEN</textPath></text>
</svg>

<svg class="label label--anis" viewBox="-300 -300 600 600">
  <defs>
    <path id="a-name" d="M -128 10 A 130 130 0 0 1 70 -110"/>
    <path id="a-claim" d="M -185 10 A 185 185 0 0 1 100 -158"/>
    <path id="a-flavour" d="M -250 50 A 255 255 0 0 0 245 70"/>
    <path id="a-use" d="M 190 190 A 270 270 0 0 0 10 -270"/>
  </defs>
  <circle cx="0" cy="0" r="297" fill="var(--anise)"/>
  <ellipse class="herb-area" cx="-160" cy="110" rx="90" ry="85" role="img" aria-label="Zeichnung eines Sternanis"/>
  <text class="claim"><textPath href="#a-claim">TRADITIONAL SWISS FORMULA</textPath></text>
  <circle class="brand-dot" cx="3" cy="3" r="92"/>
  <text class="brand-name"><textPath href="#a-name">PFEFFLING</textPath></text>
  <text class="flavour" text-anchor="middle"><textPath href="#a-flavour" startOffset="50%">ANIS</textPath></text>
  <text class="use-case"><textPath href="#a-use">BEI MAGENSCHMERZEN</textPath></text>
</svg>

<svg class="label label--ingwer" viewBox="-300 -300 600 600">
  <defs>
    <path id="i-name" d="M -128 10 A 130 130 0 0 1 70 -110"/>
    <path id="i-claim" d="M -185 10 A 185 185 0 0 1 100 -158"/>
    <path id="i-flavour" d="M -252 35 A 255 255 0 1 0 170 -195"/>
    <path id="i-use" d="M 140 -231 A 270 270 0 0 0 -228 -145"/>
  </defs>
  <circle cx="0" cy="0" r="297" fill="var(--ginger)"/>
  <ellipse class="herb-area" cx="-215" cy="20" rx="55" ry="90" role="img" aria-label="Zeichnung von Ingwerwurzel und Zitronenscheibe"/>
  <text class="claim"><textPath href="#i-claim">TRADITIONAL SWISS FORMULA</textPath></text>
  <circle class="brand-dot" cx="3" cy="3" r="92"/>
  <text class="brand-name"><textPath href="#i-name">PFEFFLING</textPath></text>
  <text class="flavour flavour--long" text-anchor="middle"><textPath href="#i-flavour" startOffset="50%">INGWER-ZITRONE</textPath></text>
  <text class="use-case" text-anchor="middle"><textPath href="#i-use" startOffset="50%">FÜR DIE NERVEN</textPath></text>
</svg>

</body>
</html>
```